Painting Company Business Card

Brightwell Painting needs a new business card. See attachments for our logo and current card as an example.
We want to utilize the same colors in the logo, and keep all the information that is currently on it. Just need an updated and modern design.
We are open to loosing the Association Logos if it means a better design.
We are also entertaining a spot for a picture of a headshot of the person listed on the card. Head shot can be finished later.

```html
<!DOCTYPE html>
<html lang="en">
<head>
<meta charset="UTF-8">
<title>Brightwell Painting – Business Card Back</title>
<link rel="stylesheet" href="https://fonts.googleapis.com/css2?family=Montserrat:wght@400;500&display=swap">
<style>
  :root {
    --wall-base: #9c4e50;
    --wall-light: #a85a5b;
    --wall-dark: #8c4346;
    --brand-tone: #d08c7e;
    --text-light: #ffffff;
  }
  html, body {
    margin: 0;
    padding: 0;
    width: 1200px;
    height: 686px;
    overflow: hidden;
    background: var(--wall-base);
  }
  .card {
    position: relative;
    width: 1200px;
    height: 686px;
    overflow: hidden;
    font-family: "Montserrat", sans-serif;
  }
  .card__texture {
    position: absolute;
    inset: 0;
    background:
      radial-gradient(ellipse at 50% 45%, var(--wall-light) 0%, var(--wall-base) 55%, var(--wall-dark) 100%);
  }
  .brand-name {
    position: absolute;
    left: 0;
    right: 0;
    top: 236px;
    margin: 0;
    text-align: center;
    color: var(--brand-tone);
    font-weight: 500;
    font-size: 56px;
    line-height: 1.15;
    letter-spacing: 0.06em;
    text-transform: uppercase;
  }
  .brand-name__line {
    display: block;
  }
  .web-address {
    position: absolute;
    left: 0;
    right: 0;
    top: 486px;
    margin: 0;
    text-align: center;
    color: var(--text-light);
    font-weight: 400;
    font-size: 34px;
    letter-spacing: 0.01em;
  }
</style>
</head>
<body>
  <main class="card">
    <div class="card__texture" role="img" aria-label="Textured red stucco wall background"></div>
    <h1 class="brand-name">
      <span class="brand-name__line">Brightwell</span>
      <span class="brand-name__line">Painting</span>
    </h1>
    <p class="web-address">www.brightwellpainting.com</p>
  </main>
</body>
</html>
```